Va-Runel Sweetened Condensed Creamer

This project calls for a logo/packaging design for sweetened condensed creamer

Brand Name: Va-Runel (note: hyphen must be used)

Size:13.25 fl oz (375g)

Image: Incorporate a cow in the design close to the brand name Va-Runel

Blurbs: "sweetened condensed creamer"

Background:
plate served with flan pastry

feel free to change the colors and design layout

Target Market(s)

First and second generation Hispanic, Spanish speaking and price conscious
consumers

Industry/Entity Type

Grocery Store

Requirements
Must have
• cow close to the logo (head of cow or in full)
• Distributed By:
• Harbor Depot
• Ferndale, CA 90077
• harbordepot.example

```html
<!DOCTYPE html>
<html lang="en">
<head>
<meta charset="utf-8">
<title>Va-Runel Sweetened Condensed Creamer – Label</title>
<link rel="stylesheet" href="https://fonts.googleapis.com/css2?family=Arimo:wght@400;700&family=Lilita+One&family=Anton&display=swap">
<style>
  :root {
    --stage: #e9e4d8;
    --cream-top: #fffcee;
    --cream-mid: #fde9b4;
    --cream-bottom: #f6c259;
    --brand-blue: #1f47c9;
    --ink: #111111;
    --badge-red: #e3141b;
    --white: #ffffff;
    --caramel-light: #e9a64a;
    --caramel-dark: #9c4410;
  }
  * { box-sizing: border-box; margin: 0; padding: 0; }
  html, body {
    width: 1200px; height: 546px; overflow: hidden;
    background: var(--stage);
    font-family: "Arimo", Arial, sans-serif;
  }
  .label {
    position: absolute; left: 26px; top: 42px;
    width: 1149px; height: 340px; overflow: hidden;
    background: linear-gradient(180deg, var(--cream-top) 0%, var(--cream-mid) 55%, var(--cream-bottom) 100%);
  }
  .label-wave { position: absolute; inset: 0; width: 100%; height: 100%; }
  .backdrop-glow {
    position: absolute; left: 445px; top: 2px; width: 330px; height: 195px;
    border-radius: 50%;
    background: radial-gradient(ellipse at center, rgba(255,255,255,.9) 0%, rgba(255,255,255,.5) 60%, rgba(255,255,255,0) 100%);
  }

  /* Nutrition panel */
  .nutrition {
    position: absolute; left: 66px; top: 20px; width: 181px; height: 300px;
    background: var(--white); border: 1.5px solid var(--ink);
    padding: 2px 4px; color: var(--ink);
    font-size: 9px; line-height: 10px;
    display: flex; flex-direction: column;
  }
  .nutrition h2 { font-size: 23px; font-weight: 700; line-height: 23px; letter-spacing: -.3px; }
  .nutrition .rule-heavy { border-top: 5px solid var(--ink); margin: 2px 0; }
  .nutrition .rule-mid { border-top: 3px solid var(--ink); margin: 1px 0; }
  .nutrition .row {
    display: flex; justify-content: space-between;
    border-top: 1px solid var(--ink); padding: 1px 0;
  }
  .nutrition .row.plain { border-top: none; }
  .nutrition .row.indent { padding-left: 14px; }
  .nutrition .small { font-size: 7px; line-height: 8px; }
  .nutrition .right { text-align: right; }
  .nutrition .footnote {
    margin-top: auto; font-size: 6.4px; line-height: 7.6px;
    border-top: 1px solid var(--ink); padding-top: 2px;
  }

  /* Trans fat badge */
  .trans-badge {
    position: absolute; left: 292px; top: 0; width: 82px; height: 96px;
    background: var(--badge-red); color: var(--white); text-align: center;
    font-weight: 700; padding-top: 28px; line-height: 1;
    clip-path: polygon(0 0, 100% 0, 100% 92%, 50% 100%, 0 92%);
  }
  .trans-badge .small { font-size: 11px; display: block; }
  .trans-badge .big { font-size: 19px; display: block; letter-spacing: -.8px; transform: scaleX(.85); margin: 2px 0; }

  /* Brand */
  .brand-name {
    position: absolute; left: 416px; top: 64px; width: 334px; text-align: center;
    font-family: "Lilita One", sans-serif; font-size: 68px; font-weight: 400;
    color: var(--brand-blue); line-height: 1;
  }
  .product-name {
    position: absolute; left: 281px; top: 140px;
    font-family: "Lilita One", sans-serif; font-size: 35px; line-height: 33px;
    color: var(--white); -webkit-text-stroke: 1.6px var(--brand-blue);
    letter-spacing: -.5px;
  }
  .product-name span { display: block; }
  .product-name .l3 { padding-left: 56px; }

  .serving-image {
    position: absolute; left: 470px; top: 142px; width: 280px; height: 148px;
    border-radius: 14px;
    background: linear-gradient(180deg, var(--caramel-light) 0%, var(--caramel-dark) 100%);
  }

  .net-weight {
    position: absolute; left: 450px; top: 294px; width: 280px; text-align: center;
    font-family: "Anton", sans-serif; font-size: 24px; line-height: 1;
    color: var(--white); -webkit-text-stroke: 1px var(--ink);
    letter-spacing: -.5px;
  }

  /* Info column */
  .info {
    position: absolute; left: 823px; top: 18px; width: 262px;
    color: var(--ink); font-size: 11px; line-height: 13px;
  }
  .info p { text-align: justify; }
  .info strong { font-weight: 700; }
  .info .gap { margin-top: 10px; }
  .code-window {
    position: absolute; left: 841px; top: 220px; width: 174px; height: 74px;
    background: var(--white);
  }
  .code-note {
    position: absolute; left: 820px; top: 298px; width: 216px; text-align: center;
    font-size: 11px; line-height: 13px; color: var(--ink);
  }
  .seam-strip {
    position: absolute; left: 1124px; top: 16px; width: 25px; height: 308px;
    background: var(--white);
  }
</style>
</head>
<body>
  <main class="label">
    <svg class="label-wave" viewBox="0 0 1149 340" preserveAspectRatio="none" aria-hidden="true">
      <path d="M0 250 C 300 240, 600 170, 1149 180 L1149 230 C 700 215, 350 270, 0 290 Z" fill="#ffffff" opacity=".55"/>
    </svg>
    <div class="backdrop-glow"></div>

    <section class="nutrition" aria-label="Nutrition Facts">
      <h2>Nutrition Facts</h2>
      <div>Serving Size 2 tb sp (39g)</div>
      <div>Servings Per Container About 10</div>
      <div class="rule-heavy"></div>
      <div class="small">Amount Per Serving</div>
      <div class="row plain"><span><b>Calories</b> 130</span><span>Calories from Fat 35</span></div>
      <div class="rule-mid"></div>
      <div class="small right">% Daily Values*</div>
      <div class="row"><b>Total Fat 4g</b><b>6%</b></div>
      <div class="row indent"><span>Saturated Fat 2g</span><b>10%</b></div>
      <div class="row indent"><span><i>Trans</i> Fat 0g</span><span></span></div>
      <div class="row"><span><b>Cholesterol</b> 0mg</span><b>0%</b></div>
      <div class="row"><span><b>Sodium</b> 45mg</span><b>2%</b></div>
      <div class="row"><span><b>Total Carbohydrate</b> 24g</span><b>8%</b></div>
      <div class="row indent"><span>Dietary Fiber 0g</span><b>0%</b></div>
      <div class="row indent"><span>Sugars 19g</span><span></span></div>
      <div class="row"><b>Protein 1g</b><b>2%</b></div>
      <div class="rule-heavy"></div>
      <div class="row plain"><span>Vitamin A &nbsp; 0%</span><span>• &nbsp;Vitamin C &nbsp; 0%</span></div>
      <div class="row"><span>Calcium &nbsp; &nbsp; 6%</span><span>• &nbsp; &nbsp; &nbsp; Iron &nbsp; 6%</span></div>
      <div class="row"><span>Vitamin D &nbsp; 2%</span></div>
      <p class="footnote">*Percent Daily Values are based on a 2,000 calorie diet. Your Daily Values may be higher or lower depending on your calorie needs</p>
    </section>

    <div class="trans-badge">
      <span class="small">0 grams</span>
      <span class="big">Trans Fat</span>
      <span class="small">per serving</span>
    </div>

    <div class="serving-image" role="img" aria-label="Photo of flan with caramel sauce and a strawberry on a white plate"></div>

    <h1 class="brand-name">Va-Runel</h1>

    <div class="product-name">
      <span>Sweetened</span>
      <span>Condensed</span>
      <span class="l3">Creamer</span>
    </div>

    <div class="net-weight">NET WT.13.25fl oz(375g)</div>

    <section class="info">
      <p><strong>INGREDIENTS:</strong> Sugar, Water, Whey Powder, Vegetable Oil (Refined Palm Oil), Skimmed Milk Powder, Butter Milk Powder, Tetrasodium Pyrophosphate, Titanium Dioxide, Sodium Stearoyl lactylate, Soy Lecithin, Xanthan Gum, Lactose, Vitamin A, Vitamin B1 and Vitamin D3.</p>
      <div><strong>CONTAINS MILK AND SOY INGREDIENTS.</strong></div>
      <div><strong>PRODUCT OF MALAYSIA</strong></div>
      <div>Distributed By:</div>
      <div><strong>Harbor Depot</strong></div>
      <div>Ferndale, CA 90077</div>
      <div>harbordepot.example</div>
      <p class="gap"><strong>CAUTION:</strong> Never Heat Unopened. Keep in a Fresh and dry Place, Refrigerate After Opening.</p>
    </section>

    <div class="code-window"></div>
    <p class="code-note">Best Before and Lot Number<br>printed on the top</p>
    <div class="seam-strip"></div>
  </main>
</body>
</html>
```